Book Cover Design Project

I need book cover graphics for 2/4 short pdf monographs
Titles:
1. What Hides Behind the Gastric Band?
Plain Facts on Hazards and Setbacks
2. 7 Facts Every Obesity Doctor Keeps Quiet
I want to use the same/similar cover design a second time for Plastic (Cosmetic) Surgery so the covers should be generic medical, perhaps with some images reference to beauty in the case or Plastic Surgery and weight loss in the case of Bariatric Surgery. You would just change the title block to refer to the other specialty, substituting Cosmetic for Weight Loss and Plastic for Bariatric.
Size is 6"x9" or A5

```html
<!DOCTYPE html>
<html lang="en">
<head>
<meta charset="utf-8">
<title>7 Facts Every Obesity Doctor Keeps Quiet</title>
<link rel="stylesheet" href="https://fonts.googleapis.com/css2?family=Poiret+One&display=swap">
<style>
  :root {
    --page: #ffffff;
    --cover-grey: #dcdbdf;
    --ink: #0d0d0d;
    --scrub-teal: #a9dcd2;
    --mask-blue: #c9e6f4;
    --cap-aqua: #6fd0d6;
    --skin: #d9b39a;
  }
  html, body {
    margin: 0;
    width: 1000px;
    height: 1200px;
    overflow: hidden;
    background: var(--page);
  }
  .book-cover {
    position: absolute;
    left: 150px;
    top: 43px;
    width: 743px;
    height: 1117px;
    background: var(--cover-grey);
    box-shadow: -4px 6px 10px rgba(0,0,0,0.35);
    overflow: hidden;
  }
  .cover-art {
    position: absolute;
    inset: 0;
  }
  .title-block {
    position: absolute;
    inset: 0;
    font-family: "Poiret One", sans-serif;
    fill: var(--ink);
  }
  .title-number {
    font-size: 330px;
  }
  .title-line {
    font-size: 108px;
  }
</style>
</head>
<body>
  <div class="book-cover">
    <svg class="cover-art" width="743" height="1117" viewBox="150 43 743 1117">
      <defs>
        <linearGradient id="surgeon-tones" x1="0" y1="0" x2="0" y2="1">
          <stop offset="0" stop-color="var(--cap-aqua)"/>
          <stop offset="0.22" stop-color="var(--skin)"/>
          <stop offset="0.38" stop-color="var(--mask-blue)"/>
          <stop offset="0.62" stop-color="var(--mask-blue)"/>
          <stop offset="0.75" stop-color="var(--skin)"/>
          <stop offset="1" stop-color="var(--scrub-teal)"/>
        </linearGradient>
      </defs>
      <path role="img" aria-label="Photo of a surgeon in cap, face mask and green scrubs, looking at the viewer"
            fill="url(#surgeon-tones)"
            d="M540,43 L893,43 L893,1160 L460,1160 C520,1000 640,900 720,840 C780,800 820,780 815,730 C760,640 690,560 650,480 C615,430 600,380 590,330 C570,250 545,150 540,43 Z"/>
    </svg>

    <svg class="title-block" width="743" height="1117" viewBox="150 43 743 1117">
      <text class="title-number" x="362" y="330" text-anchor="middle">7</text>
      <rect class="title-rule" x="243" y="350" width="235" height="8" fill="var(--ink)"/>
      <text class="title-line" x="170" y="465" textLength="410" lengthAdjust="spacing">FACTS</text>
      <text class="title-line" x="170" y="595" textLength="410" lengthAdjust="spacing">EVERY</text>
      <text class="title-line" x="170" y="725" textLength="410" lengthAdjust="spacingAndGlyphs">OBESITY</text>
      <text class="title-line" x="170" y="855" textLength="410" lengthAdjust="spacingAndGlyphs">DOCTOR</text>
      <text class="title-line" x="170" y="985" textLength="410" lengthAdjust="spacing">KEEPS</text>
      <text class="title-line" x="170" y="1115" textLength="410" lengthAdjust="spacing">QUIET</text>
    </svg>
  </div>
</body>
</html>
```